Penny auction website for high end market

need a penny auction web design , requirement as below :-

- classy and noble, as i am only selli high end products
- 25 products for the main page , 5 products per row ( please see sample picture )
- top 5 products can be highlighted as those are limited edition products
- main page , products page, members page , faq and about us page
- matching logo with the name lotvo
- clean
- responsive for desktoop
-mobile version
Updates

i missed the mobile version, i should get the mobile version aswell, for desktop it should be responsive Added Wednesday, August 16, 2017

designer may use gold or silver color too as i am selling only high end products exclusively for members only, the layout can be different than the sample, it just a guide line for the sample, other better layout would be great to see and to have.

some idea how highend feel to me https://img.kravelshop.example/scr/51200/shining-gems-flash-cms-layout_52716-original.jpg

guys, please use this design https://www.pagewrenhub.example/flash-cms-layouts/52716.html as the base , i want it high class and up market, thanks

Target Market(s)

highend products buyer

Number of Pages Required

5+ page

Font styles to use
Serif
Sans Serif
Script
Other font styles liked:
• designer match it

Colors

Designer to choose colors to be used in the design.

Requirements
Must have
• source code, logos ( use lotvo for now, will change later when confirm ) , PSD
Nice to have
• more different type of designs would be great, designers can present they ideas other than my requirement

```html
<!DOCTYPE html>
<html lang="en">
<head>
<meta charset="utf-8">
<title>lotvo – Penny Auction</title>
<link href="https://fonts.googleapis.com/css2?family=Open+Sans:wght@400;600;700;800&display=swap" rel="stylesheet">
<style>
:root{
  --blue:#1aa3dc;
  --blue-dark:#0d85c0;
  --orange:#f5a623;
  --orange-dark:#e8901a;
  --text:#555;
  --muted:#999;
  --line:#e3e8ec;
  --band:#eef3f6;
  --white:#fff;
  --sold:#d9d9d9;
  --stamp:#d62b2b;
}
*{margin:0;padding:0;box-sizing:border-box}
html,body{width:1200px;height:3100px;overflow:hidden;background:var(--white)}
body{font-family:"Open Sans",Arial,sans-serif;color:var(--text);position:relative}

/* header */
.site-header{position:absolute;top:0;left:0;width:1200px;height:64px;padding:0 50px;display:flex;align-items:center;justify-content:space-between}
.brand{display:flex;align-items:center;gap:10px;font-size:34px;font-weight:800;color:var(--blue);letter-spacing:-.5px}
.brand-mark{width:14px;height:14px;border-radius:50%;background:var(--orange)}
.header-right{display:flex;flex-direction:column;align-items:flex-end;gap:6px}
.utility{display:flex;align-items:center;gap:16px;font-size:11px;color:var(--muted)}
.utility span::before{content:"";display:inline-block;width:7px;height:7px;border-radius:50%;background:var(--orange);margin-right:5px;vertical-align:middle}
.search{width:120px;height:20px;border:1px solid var(--line);border-radius:3px}
.main-nav{display:flex;gap:4px;font-size:13px;font-weight:600}
.main-nav a{color:#444;text-decoration:none;padding:4px 12px}
.main-nav a.active{background:var(--blue);color:var(--white);border-radius:2px}

/* hero */
.hero{position:absolute;top:64px;left:0;width:1200px;height:500px;overflow:hidden}
.hero-photo{position:absolute;inset:0;background:linear-gradient(100deg,#cfd3d6 0%,#a9a9a6 40%,#7d7469 70%,#5a4e44 100%)}
.hero-shape{position:absolute;inset:0}
.hero-products{position:absolute;left:60px;top:40px;width:380px;height:360px;border-radius:24px;background:linear-gradient(160deg,#3a3f46,#8b959e);opacity:.85}
.hero-copy{position:absolute;left:690px;top:150px;width:440px;color:var(--white)}
.hero-copy h1{font-size:56px;font-weight:800;line-height:1.1;text-shadow:0 2px 6px rgba(0,0,0,.25)}
.hero-copy p{margin-top:12px;font-size:14px;line-height:1.5}
.hero-btn{display:inline-block;margin-top:24px;background:var(--orange);color:var(--white);font-size:13px;font-weight:700;padding:10px 22px;border-radius:3px}
.hero-dots{position:absolute;left:560px;bottom:48px;display:flex;gap:10px}
.hero-dots i{width:12px;height:12px;border-radius:50%;background:#bcd;display:block}
.hero-dots i:first-child{background:var(--blue)}

/* auction section */
.auction{position:absolute;top:600px;left:50px;width:1100px}
.auction-title{text-align:center;font-size:30px;font-weight:700;color:var(--blue)}
.auction-intro{text-align:center;font-size:12px;color:var(--muted);width:640px;margin:8px auto 0;line-height:1.5}
.auction-grid{margin-top:26px;display:flex;flex-direction:column;gap:16px}
.auction-row{display:grid;grid-template-columns:repeat(5,1fr);gap:16px;padding:14px 14px;border:1px solid var(--line);height:388px}
.lot{text-align:center;display:flex;flex-direction:column;align-items:center;border:1px solid var(--line);padding:10px 8px}
.lot-title{font-size:12px;color:var(--blue);line-height:1.4;height:34px;width:140px}
.lot-image{position:relative;margin-top:10px;width:150px;height:120px;border-radius:6px}
.lot-image.dark{background:linear-gradient(150deg,#2b2e33,#6e747b)}
.lot-image.tablet{background:linear-gradient(150deg,#3a3f4a,#c2516a)}
.lot-image.phone{background:linear-gradient(150deg,#1f2226,#5a6068)}
.lot-image.card{background:linear-gradient(150deg,#202225,#4d5155)}
.lot-image.usb{background:linear-gradient(150deg,#27406d,#8aa0c4)}
.lot-image.perfume{background:linear-gradient(150deg,#e6c86b,#f3ecd6)}
.lot-image.car{background:linear-gradient(150deg,#d9dde0,#a12a36)}
.lot-image.laptop{background:linear-gradient(150deg,#c9ced3,#5d6670)}
.lot-image.monitor{background:linear-gradient(150deg,#eef0f2,#9aa3ab)}
.stamp{position:absolute;left:38px;top:42px;border:3px solid var(--stamp);color:var(--stamp);font-size:20px;font-weight:800;padding:0 8px;transform:rotate(-18deg);background:rgba(255,255,255,.6)}
.lot-timer{margin-top:14px;width:150px;height:26px;background:var(--orange);border-radius:3px;display:flex;align-items:center;justify-content:center;gap:4px;font-size:11px;color:var(--white);font-weight:700}
.lot-timer b{background:var(--orange-dark);padding:2px 5px;border-radius:2px}
.lot-old{margin-top:12px;font-size:12px;color:var(--muted);text-decoration:line-through}
.lot-price{font-size:22px;font-weight:700;color:var(--blue);line-height:1.3}
.lot-btn{margin-top:8px;width:120px;height:28px;line-height:28px;border-radius:14px;background:var(--blue);color:var(--white);font-size:11px;font-weight:700}
.lot-btn.sold{background:var(--sold);color:#777}

/* steps */
.steps{position:absolute;top:2780px;left:0;width:1200px;height:210px;background:var(--band);padding:30px 130px 0}
.step-row{display:flex}
.step{width:240px;height:56px;background:var(--blue);color:var(--white);font-size:14px;font-weight:600;display:flex;align-items:center;justify-content:center;clip-path:polygon(0 0,88% 0,100% 50%,88% 100%,0 100%,12% 50%);margin-right:-14px}
.step:first-child{clip-path:polygon(0 0,88% 0,100% 50%,88% 100%,0 100%)}
.step.start{background:var(--orange);font-weight:800;font-size:16px}
.step-notes{display:flex;margin-top:-12px}
.step-note{width:226px;text-align:center;font-size:11px;color:var(--muted);line-height:1.5}
.step-num{width:26px;height:26px;border-radius:50%;background:var(--blue);border:2px solid var(--white);color:var(--white);font-size:12px;font-weight:700;line-height:22px;margin:0 auto 10px}
.step-note.start .step-num{background:var(--orange)}

/* footer */
.site-footer{position:absolute;top:3040px;left:0;width:1200px;height:60px;padding:0 50px;display:flex;align-items:center;justify-content:space-between;font-size:11px;color:var(--muted);border-top:1px solid var(--line)}
.social{display:flex;align-items:center;gap:10px}
.social i{width:18px;height:18px;border-radius:50%;background:#c8d0d6;display:block}
</style>
</head>
<body>

<header class="site-header">
  <div class="brand"><span class="brand-mark"></span>lotvo</div>
  <div class="header-right">
    <div class="utility"><span>Watch Later</span><span>Register</span><span>Log Out</span><div class="search"></div></div>
    <nav class="main-nav">
      <a class="active" href="#">Home</a><a href="#">About</a><a href="#">Services</a><a href="#">Products</a><a href="#">Testimonials</a><a href="#">Blog</a><a href="#">Contact Us</a>
    </nav>
  </div>
</header>

<section class="hero">
  <div class="hero-photo" role="img" aria-label="Photo of a smiling shopper holding a phone"></div>
  <svg class="hero-shape" width="1200" height="500" viewBox="0 0 1200 500" aria-hidden="true">
    <path d="M0 0 H560 C520 120 600 300 520 420 C470 480 300 470 0 440 Z" fill="#1aa3dc"/>
    <path d="M0 440 C300 470 470 480 520 420 C480 500 260 500 0 480 Z" fill="#f5a623"/>
    <path d="M0 480 C260 500 480 500 520 420 C520 470 500 500 480 500 H0 Z" fill="#ffffff"/>
  </svg>
  <div class="hero-products" role="img" aria-label="Illustration of a smartphone, laptop and camera with price tags"></div>
  <div class="hero-copy">
    <h1>Penny Auction</h1>
    <p>Duis aute irure dolor in reprehenderit in voluptate velit esse cillum dolore fugiat nulla pariatur.</p>
    <span class="hero-btn">Click Here to Bid</span>
  </div>
  <div class="hero-dots"><i></i><i></i><i></i></div>
</section>

<main class="auction">
  <h2 class="auction-title">Auction Products</h2>
  <p class="auction-intro">Lorem ipsum dolor sit amet, consectetur adipiscing elit, sed do eiusmod tempor incididunt ut labore et dolore magna aliqua. Ut enim ad minim veniam quis nostrud exercitation.</p>

  <div class="auction-grid">
    <div class="auction-row">
      <div class="lot"><div class="lot-title">Eiusmod Tempor Ipsum Incididunt</div><div class="lot-image dark" role="img" aria-label="Photo of a digital camera"></div><div class="lot-timer"><b>05</b>:<b>08</b>:<b>46</b></div><div class="lot-old">$245.00</div><div class="lot-price">$147.00</div><div class="lot-btn">BID</div></div>
      <div class="lot"><div class="lot-title">Eiusmod Tempor Ipsum Incididunt</div><div class="lot-image tablet" role="img" aria-label="Photo of a tablet"></div><div class="lot-timer"><b>05</b>:<b>08</b>:<b>46</b></div><div class="lot-old">$399.00</div><div class="lot-price">$277.00</div><div class="lot-btn">BID</div></div>
      <div class="lot"><div class="lot-title">Eiusmod Tempor Ipsum Incididunt</div><div class="lot-image phone" role="img" aria-label="Photo of a smartphone"><span class="stamp">SOLD</span></div><div class="lot-timer"><b>05</b>:<b>08</b>:<b>46</b></div><div class="lot-old">$179.00</div><div class="lot-price">$80.00</div><div class="lot-btn">BID</div></div>
      <div class="lot"><div class="lot-title">Eiusmod Tempor Ipsum Incididunt</div><div class="lot-image card" role="img" aria-label="Photo of a memory card"></div><div class="lot-timer"><b>05</b>:<b>08</b>:<b>46</b></div><div class="lot-old">$99.00</div><div class="lot-price">$57.00</div><div class="lot-btn">BID</div></div>
      <div class="lot"><div class="lot-title">Eiusmod Tempor Ipsum Incididunt</div><div class="lot-image usb" role="img" aria-label="Photo of a USB drive"><span class="stamp">SOLD</span></div><div class="lot-timer"><b>05</b>:<b>08</b>:<b>46</b></div><div class="lot-old">$245.00</div><div class="lot-price">$147.00</div><div class="lot-btn sold">SOLD</div></div>
    </div>

    <div class="auction-row">
      <div class="lot"><div class="lot-title">Eiusmod Tempor Ipsum Incididunt</div><div class="lot-image perfume" role="img" aria-label="Photo of a perfume bottle"></div><div class="lot-timer"><b>05</b>:<b>08</b>:<b>46</b></div><div class="lot-old">$245.00</div><div class="lot-price">$147.00</div><div class="lot-btn">BID</div></div>
      <div class="lot"><div class="lot-title">Eiusmod Tempor Ipsum Incididunt</div><div class="lot-image car" role="img" aria-label="Photo of a toy car"><span class="stamp">SOLD</span></div><div class="lot-timer"><b>05</b>:<b>08</b>:<b>46</b></div><div class="lot-old">$399.00</div><div class="lot-price">$277.00</div><div class="lot-btn sold">SOLD</div></div>
      <div class="lot"><div class="lot-title">Eiusmod Tempor Ipsum Incididunt</div><div class="lot-image laptop" role="img" aria-label="Photo of a laptop"></div><div class="lot-timer"><b>05</b>:<b>08</b>:<b>46</b></div><div class="lot-old">$179.00</div><div class="lot-price">$80.00</div><div class="lot-btn">BID</div></div>
      <div class="lot"><div class="lot-title">Eiusmod Tempor Ipsum Incididunt</div><div class="lot-image card" role="img" aria-label="Photo of a memory card"><span class="stamp">SOLD</span></div><div class="lot-timer"><b>05</b>:<b>08</b>:<b>46</b></div><div class="lot-old">$99.00</div><div class="lot-price">$57.00</div><div class="lot-btn sold">SOLD</div></div>
      <div class="lot"><div class="lot-title">Eiusmod Tempor Ipsum Incididunt</div><div class="lot-image perfume" role="img" aria-label="Photo of a perfume bottle"></div><div class="lot-timer"><b>05</b>:<b>08</b>:<b>46</b></div><div class="lot-old">$245.00</div><div class="lot-price">$147.00</div><div class="lot-btn">BID</div></div>
    </div>

    <div class="auction-row">
      <div class="lot"><div class="lot-title">Eiusmod Tempor Ipsum Incididunt</div><div class="lot-image dark" role="img" aria-label="Photo of a digital camera"></div><div class="lot-timer"><b>05</b>:<b>08</b>:<b>46</b></div><div class="lot-old">$245.00</div><div class="lot-price">$147.00</div><div class="lot-btn">BID</div></div>
      <div class="lot"><div class="lot-title">Eiusmod Tempor Ipsum Incididunt</div><div class="lot-image tablet" role="img" aria-label="Photo of a tablet"><span class="stamp">SOLD</span></div><div class="lot-timer"><b>05</b>:<b>08</b>:<b>46</b></div><div class="lot-old">$399.00</div><div class="lot-price">$277.00</div><div class="lot-btn sold">SOLD</div></div>
      <div class="lot"><div class="lot-title">Eiusmod Tempor Ipsum Incididunt</div><div class="lot-image phone" role="img" aria-label="Photo of a smartphone"><span class="stamp">SOLD</span></div><div class="lot-timer"><b>05</b>:<b>08</b>:<b>46</b></div><div class="lot-old">$179.00</div><div class="lot-price">$80.00</div><div class="lot-btn sold">SOLD</div></div>
      <div class="lot"><div class="lot-title">Eiusmod Tempor Ipsum Incididunt</div><div class="lot-image card" role="img" aria-label="Photo of a memory card"></div><div class="lot-timer"><b>05</b>:<b>08</b>:<b>46</b></div><div class="lot-old">$99.00</div><div class="lot-price">$57.00</div><div class="lot-btn">BID</div></div>
      <div class="lot"><div class="lot-title">Eiusmod Tempor Ipsum Incididunt</div><div class="lot-image usb" role="img" aria-label="Photo of a USB drive"></div><div class="lot-timer"><b>05</b>:<b>08</b>:<b>46</b></div><div class="lot-old">$245.00</div><div class="lot-price">$147.00</div><div class="lot-btn">BID</div></div>
    </div>

    <div class="auction-row">
      <div class="lot"><div class="lot-title">Eiusmod Tempor Ipsum Incididunt</div><div class="lot-image laptop" role="img" aria-label="Photo of a laptop"></div><div class="lot-timer"><b>05</b>:<b>08</b>:<b>46</b></div><div class="lot-old">$245.00</div><div class="lot-price">$147.00</div><div class="lot-btn">BID</div></div>
      <div class="lot"><div class="lot-title">Eiusmod Tempor Ipsum Incididunt</div><div class="lot-image monitor" role="img" aria-label="Photo of a camcorder"></div><div class="lot-timer"><b>05</b>:<b>08</b>:<b>46</b></div><div class="lot-old">$399.00</div><div class="lot-price">$277.00</div><div class="lot-btn">BID</div></div>
      <div class="lot"><div class="lot-title">Eiusmod Tempor Ipsum Incididunt</div><div class="lot-image dark" role="img" aria-label="Photo of a DSLR camera"></div><div class="lot-timer"><b>05</b>:<b>08</b>:<b>46</b></div><div class="lot-old">$179.00</div><div class="lot-price">$80.00</div><div class="lot-btn">BID</div></div>
      <div class="lot"><div class="lot-title">Eiusmod Tempor Ipsum Incididunt</div><div class="lot-image phone" role="img" aria-label="Photo of a smartphone"></div><div class="lot-timer"><b>05</b>:<b>08</b>:<b>46</b></div><div class="lot-old">$99.00</div><div class="lot-price">$57.00</div><div class="lot-btn">BID</div></div>
      <div class="lot"><div class="lot-title">Eiusmod Tempor Ipsum Incididunt</div><div class="lot-image monitor" role="img" aria-label="Photo of a desktop monitor"></div><div class="lot-timer"><b>05</b>:<b>08</b>:<b>46</b></div><div class="lot-old">$245.00</div><div class="lot-price">$147.00</div><div class="lot-btn">BID</div></div>
    </div>

    <div class="auction-row">
      <div class="lot"><div class="lot-title">Eiusmod Tempor Ipsum Incididunt</div><div class="lot-image perfume" role="img" aria-label="Photo of a perfume bottle"></div><div class="lot-timer"><b>05</b>:<b>08</b>:<b>46</b></div><div class="lot-old">$245.00</div><div class="lot-price">$147.00</div><div class="lot-btn">BID</div></div>
      <div class="lot"><div class="lot-title">Eiusmod Tempor Ipsum Incididunt</div><div class="lot-image car" role="img" aria-label="Photo of a toy car"><span class="stamp">SOLD</span></div><div class="lot-timer"><b>05</b>:<b>08</b>:<b>46</b></div><div class="lot-old">$399.00</div><div class="lot-price">$277.00</div><div class="lot-btn sold">SOLD</div></div>
      <div class="lot"><div class="lot-title">Eiusmod Tempor Ipsum Incididunt</div><div class="lot-image laptop" role="img" aria-label="Photo of a laptop"><span class="stamp">SOLD</span></div><div class="lot-timer"><b>05</b>:<b>08</b>:<b>46</b></div><div class="lot-old">$179.00</div><div class="lot-price">$80.00</div><div class="lot-btn sold">SOLD</div></div>
      <div class="lot"><div class="lot-title">Eiusmod Tempor Ipsum Incididunt</div><div class="lot-image monitor" role="img" aria-label="Photo of a smartphone"></div><div class="lot-timer"><b>05</b>:<b>08</b>:<b>46</b></div><div class="lot-old">$99.00</div><div class="lot-price">$57.00</div><div class="lot-btn">BID</div></div>
      <div class="lot"><div class="lot-title">Eiusmod Tempor Ipsum Incididunt</div><div class="lot-image perfume" role="img" aria-label="Photo of a perfume bottle"></div><div class="lot-timer"><b>05</b>:<b>08</b>:<b>46</b></div><div class="lot-old">$245.00</div><div class="lot-price">$147.00</div><div class="lot-btn">BID</div></div>
    </div>
  </div>
</main>

<section class="steps">
  <div class="step-row">
    <div class="step">Create An Account</div>
    <div class="step">Choose Your Products</div>
    <div class="step">Bid n Win</div>
    <div class="step start">START NOW</div>
  </div>
  <div class="step-notes">
    <div class="step-note"><div class="step-num">1</div>Lorem ipsum dolor sit amet, consectetur adipiscing elit.</div>
    <div class="step-note"><div class="step-num">2</div>Lorem ipsum dolor sit amet, consectetur adipiscing elit.</div>
    <div class="step-note"><div class="step-num">3</div>Lorem ipsum dolor sit amet, consectetur adipiscing elit.</div>
    <div class="step-note start"><div class="step-num">4</div></div>
  </div>
</section>

<footer class="site-footer">
  <span>Copyright © 2017 – lotvo Inc. All rights reserved.</span>
  <div class="social"><span>Connect With Us</span><i></i><i></i><i></i><i></i><i></i></div>
</footer>

</body>
</html>
```